New Branding Logo and Stationery Design Project

We are looking for a Stationary design for a company called "Peak Renewal". We are a Personal Training business that helps people of diverse ages, fitness levels and goals achieve what they aspire to. We are excellent at what we do and have a high rate of results. We are highly compassionate and love helping people. We want this to show in our logo. The logo must be able to be used on websites but also allow for large printing in the future also.

On the Business Card
Front we need the logo, and underneath this the words "Your health and fitness specialists".
On the back of the card we need:
Name (this will be different on the 2 peoples cards)
Health and fitness specialist
mobile: 04XX-XXX-XXX (we will give to the winner to add)
website: www.peakrenewal-example.com.au
email: info@peakrenewal-example.com.au
Down the bottom of the card we need a section that says something like:
"Your next appointment date is / / time : "

On the letterhead we will need:
Logo
Peak Renewal Pty Ltd
Address
Phone number
Email
Website

Target Market(s)

Anyone, any age who needs help with health and fitness

Industry/Entity Type

Printing

Requirements
Must have
• Templates for business cards here:
https://www.inkmarlow-example.com.au/businesscards_diy.php
Should not have
• Should not be Racist, Sexist, Ageist

```html
<!DOCTYPE html>
<html lang="en">
<head>
<meta charset="utf-8">
<title>Peak Renewal Stationery</title>
<link rel="stylesheet" href="https://fonts.googleapis.com/css2?family=Source+Sans+3:ital,wght@0,400;0,700;1,400;1,700&family=Tinos&family=Arimo:ital,wght@0,400;0,700;1,700&family=Pinyon+Script&display=swap">
<style>
  :root {
    --plum: #2e0a36;
    --magenta: #d23ccc;
    --cream: #f4efa6;
    --yellow: #f3d700;
    --cyan: #5fd3ee;
    --olive: #8fa012;
    --ink: #000000;
    --text: #333333;
    --paper: #ffffff;
    --backdrop: #ece8df;
  }
  * { margin: 0; padding: 0; box-sizing: border-box; }
  html, body { width: 1200px; height: 900px; overflow: hidden; }
  body { position: relative; background: var(--backdrop); font-family: "Arimo", sans-serif; }

  /* Letterhead */
  .letterhead {
    position: absolute; left: 134px; top: 36px; width: 564px; height: 792px;
    background: var(--paper); box-shadow: 0 2px 10px rgba(0,0,0,.18);
  }
  .letterhead__wave { position: absolute; left: 0; top: 0; width: 564px; height: 80px; }
  .brand { position: absolute; left: 34px; top: 36px; width: 150px; text-align: center; }
  .brand__mark { display: block; width: 118px; height: 118px; margin: 0 auto 6px; border-radius: 50%; background: var(--cyan); }
  .brand__name { font-family: "Source Sans 3", sans-serif; font-weight: 700; font-size: 16px; color: var(--ink); line-height: 1; }
  .brand__tagline { font-family: "Source Sans 3", sans-serif; font-style: italic; font-size: 10.5px; color: var(--text); margin-top: 2px; }
  .letter {
    position: absolute; left: 39px; top: 205px; width: 500px;
    font-family: "Tinos", serif; font-size: 12.3px; line-height: 15px; color: var(--text);
  }
  .letter p { text-align: justify; margin-bottom: 15px; }
  .letter__date { margin-bottom: 30px !important; }
  .letter__signature { font-family: "Pinyon Script", cursive; font-size: 24px; color: var(--ink); margin: 10px 0 4px !important; line-height: 1.1; }
  .letterhead__footer {
    position: absolute; left: 0; bottom: 0; width: 100%; height: 73px; background: var(--plum);
    color: var(--paper); font-family: "Tinos", serif; font-weight: 700; font-size: 11.5px; text-align: center; padding-top: 10px; line-height: 16px;
  }
  .letterhead__footer b { margin-left: 12px; }
  .letterhead__footer b:first-child { margin-left: 0; }

  /* Labels */
  .label { position: absolute; font-family: "Source Sans 3", sans-serif; font-weight: 700; font-size: 29px; line-height: 35px; color: var(--plum); }
  .label--letterhead { left: 840px; top: 150px; }
  .label--card { left: 840px; top: 236px; }
  .arrow { position: absolute; }

  /* Colour scheme */
  .scheme { position: absolute; left: 1153px; top: 22px; display: flex; flex-direction: column; gap: 3px; }
  .scheme span { width: 15px; height: 15px; display: block; }
  .scheme__title {
    position: absolute; left: 1126px; top: 20px; writing-mode: vertical-rl;
    font-family: "Source Sans 3", sans-serif; font-weight: 700; font-size: 19px; color: var(--paper); letter-spacing: .5px;
  }

  /* Card back */
  .card { position: absolute; width: 300px; height: 207px; background: var(--paper); box-shadow: 0 2px 8px rgba(0,0,0,.2); overflow: hidden; }
  .card--back { left: 806px; top: 329px; }
  .card__wave { position: absolute; left: 0; top: 0; width: 300px; height: 46px; }
  .contact { position: absolute; left: 23px; top: 50px; font-size: 11px; line-height: 13.4px; color: var(--ink); }
  .contact__name { font-weight: 700; font-size: 13.5px; line-height: 15px; }
  .contact__role, .contact__appointment { font-weight: 700; font-style: italic; }
  .contact__appointment { margin-top: 2px; }
  .appointment-line { position: absolute; left: 23px; top: 173px; font-size: 11px; font-weight: 700; font-style: italic; display: flex; align-items: flex-end; }
  .appointment-line i.rule { display: inline-block; height: 1px; background: var(--ink); margin: 0 6px 2px 2px; }

  /* Card front */
  .card--front { left: 808px; top: 619px; }
  .stripe { position: absolute; left: 0; width: 100%; }
  .stripe--sun { top: 0; height: 36px; background: linear-gradient(to bottom, var(--yellow), var(--cream)); }
  .stripe--magenta { top: 36px; height: 27px; background: linear-gradient(to right, var(--magenta), #f39fd6 70%, var(--magenta)); }
  .stripe--plum { top: 63px; height: 26px; background: linear-gradient(to right, var(--plum), #6a2a70 70%, var(--plum)); }
  .stripe--black { top: 89px; height: 24px; background: linear-gradient(to right, #000, #555 70%, #000); }
  .card__mark { position: absolute; left: 133px; top: 19px; width: 124px; height: 124px; border-radius: 50%; background: var(--cyan); }
  .card__brand { position: absolute; right: 25px; top: 152px; text-align: right; font-family: "Source Sans 3", sans-serif; }
  .card__brand-name { font-weight: 700; font-size: 16px; color: var(--ink); line-height: 1; }
  .card__brand-tagline { font-style: italic; font-size: 11px; color: var(--text); }
</style>
</head>
<body>

<article class="letterhead">
  <svg class="letterhead__wave" viewBox="0 0 564 80" preserveAspectRatio="none" aria-hidden="true">
    <path d="M0 0H564V64C500 58 440 40 370 38C300 36 250 20 170 28C110 34 60 48 0 56Z" fill="var(--plum)"/>
  </svg>
  <div class="brand">
    <span class="brand__mark"></span>
    <div class="brand__name">Peak Renewal</div>
    <div class="brand__tagline">your health &amp; fitness specialists</div>
  </div>
  <div class="letter">
    <p class="letter__date">5 July 2013</p>
    <p>Lorem ipsum,</p>
    <p>Dolor sit amet, consectetuer adipiscing elit, sed diam nonummy nibh euismod tincidunt ut laoreet dolore magna aliquam erat volutpat. Ut wisi enim ad minim veniam, quis nostrud exerci tation ullamcorper suscipit lobortis nisl ut aliquip ex ea commodo consequat.</p>
    <p>Duis autem vel eum iriure dolor in hendrerit in vulputate velit esse molestie consequat, vel illum dolore eu feugiat nulla facilisis at vero eros et accumsan et iusto odio dignissim qui blandit praesent luptatum zzril delenit augue duis dolore te feugait nulla facilisi. Nam liber tempor cum soluta nobis eleifend option congue nihil imperdiet doming id quod mazim placerat facer possim assum.</p>
    <p>Typi non habent claritatem insitam; est usus legentis in iis qui facit eorum claritatem. Investigationes demonstraverunt lectores legere me lius quod ii legunt saepius. Claritas est etiam processus dynamicus, qui sequitur mutationem consuetudium lectorum. Mirum est notare quam littera gothica, quam nunc putamus parum claram, anteposuerit litterarum formas humanitatis per seacula quarta decima et quinta decima.</p>
    <p>Eodem modo typi, qui nunc nobis videntur parum clari, fiant sollemnes in futurum.</p>
    <p class="letter__signature">Your Name</p>
    <p>Fitness Director</p>
  </div>
  <footer class="letterhead__footer">
    <div>1/88 Coral Terrace, Seabrook, QLD, Australia 4299</div>
    <div><b>P:</b> 04XX-XXX-XXX <b>E:</b> info@peakrenewal-example.com.au <b>www.peakrenewal-example.com.au</b></div>
  </footer>
</article>

<svg class="arrow" style="left:795px;top:160px" width="44" height="30" viewBox="0 0 44 30" aria-hidden="true"><path d="M0 15L44 0V30Z" fill="var(--paper)"/></svg>
<div class="label label--letterhead">Peak Renewal<br>Letterhead</div>
<svg class="arrow" style="left:803px;top:247px" width="34" height="40" viewBox="0 0 34 40" aria-hidden="true"><path d="M0 0H34L17 40Z" fill="var(--paper)"/></svg>
<div class="label label--card">Peak Renewal<br>Business Card</div>

<div class="scheme__title">color scheme</div>
<div class="scheme" aria-label="Colour scheme">
  <span style="background:var(--ink)"></span>
  <span style="background:var(--plum)"></span>
  <span style="background:var(--magenta)"></span>
  <span style="background:var(--cream)"></span>
  <span style="background:var(--yellow)"></span>
  <span style="background:var(--cyan)"></span>
  <span style="background:var(--olive)"></span>
</div>

<section class="card card--back">
  <svg class="card__wave" viewBox="0 0 300 46" preserveAspectRatio="none" aria-hidden="true">
    <path d="M0 0H300V36C260 28 220 14 170 18C130 21 110 36 60 34C35 33 15 28 0 26Z" fill="var(--plum)"/>
  </svg>
  <div class="contact">
    <div class="contact__name">John Doe</div>
    <div class="contact__role">Health &amp; Fitness Specialist</div>
    <div>1-88 Coral Terrace</div>
    <div>Seabrook QLD Australia 4299</div>
    <div><b>P:</b> 04XX-XXX-XXX</div>
    <div><b>E:</b> info@peakrenewal-example.com.au</div>
    <div>www.peakrenewal-example.com.au</div>
    <div class="contact__appointment">your next appointment is:</div>
  </div>
  <div class="appointment-line">date <i class="rule" style="width:118px"></i> at <i class="rule" style="width:94px"></i></div>
</section>

<section class="card card--front">
  <div class="stripe stripe--sun"></div>
  <div class="stripe stripe--magenta"></div>
  <div class="stripe stripe--plum"></div>
  <div class="stripe stripe--black"></div>
  <span class="card__mark"></span>
  <div class="card__brand">
    <div class="card__brand-name">Peak Renewal</div>
    <div class="card__brand-tagline">your health &amp; fitness specialists</div>
  </div>
</section>

</body>
</html>
```